Quorvel Landing page redesign

We are looking for a landing page redesign before we officially launch. We want to incorporate the information already on the site at www.Quorvel-example.com landing page but make it more inviting. There needs to be a sign up section along with clearly stating what we do. Having a place for sample profiles and linking to our blog and podcast is option. More information about all we will be doing is at Quorvel is on the landing page and also on the blog.

Target Market(s)

35 years old and up.

Coding

Coded - Design and coding required

Number of Pages Required

1 page

Requirements
Must have
• The top bar and the bottom bar (with the privacy policy, etc)
• Sign in/up section.
• I don't want to give to much here because I want designers to be creative.
Nice to have
• Prefer not to have a landing page that requires a lot of scrolling at all.

```html
<!DOCTYPE html>
<html lang="en">
<head>
<meta charset="utf-8">
<title>Quorvel</title>
<link href="https://fonts.googleapis.com/css2?family=Roboto:ital,wght@0,300;0,400;0,500;1,400&display=swap" rel="stylesheet">
<style>
:root{
  --hero:#5e6989;
  --hero-art:#6e7899;
  --ring-outer:#8f96b1;
  --ring-mid:#b9bdcf;
  --disc:#dfe1ea;
  --ink:#1f2544;
  --body-ink:#4a4d5c;
  --accent:#5c6588;
  --navy:#1b2447;
  --navy-low:#2b3763;
  --tile-a:#6b7597;
  --tile-b:#565f84;
  --tile-c:#3f4a6f;
  --footer:#2e2e2e;
  --white:#ffffff;
}
*{box-sizing:border-box;margin:0;padding:0}
html,body{width:1200px;height:1086px;overflow:hidden}
body{font-family:'Roboto',sans-serif;background:var(--hero);position:relative}
.hero{position:absolute;left:0;top:0;width:1200px;height:632px;background:var(--hero);overflow:hidden}
.hero-art{position:absolute;left:30px;top:90px;width:1140px;height:542px;
  background:radial-gradient(ellipse at 50% 70%,var(--hero-art) 0%,rgba(110,120,153,0.35) 55%,rgba(94,105,137,0) 75%)}
.nav-links{position:absolute;left:134px;top:49px;display:flex;gap:22px}
.nav-links a{color:var(--white);text-decoration:none;font-size:14.5px}
.account-links{position:absolute;left:902px;top:44px;display:flex;gap:9px}
.account-links a{display:block;width:78px;height:30px;line-height:30px;text-align:center;border-radius:15px;
  background:var(--white);color:var(--accent);text-decoration:none;font-size:14.5px}
.ring{position:absolute;border-radius:50%}
.ring-outer{left:328px;top:46px;width:544px;height:544px;background:var(--ring-outer);box-shadow:0 10px 40px rgba(40,48,80,.45)}
.ring-mid{left:356px;top:73px;width:490px;height:490px;background:var(--ring-mid)}
.disc{left:389px;top:105px;width:425px;height:425px;background:var(--disc)}
.intro{position:absolute;left:418px;top:222px;width:364px;text-align:center}
.brand-name{display:block;font-size:27px;font-weight:500;color:var(--ink);margin-bottom:14px}
.intro p{font-size:17px;line-height:27px;color:var(--body-ink)}
.intro p em{font-style:italic}
.samples{position:absolute;left:429px;top:360px;display:flex;gap:6px}
.samples a{display:block;width:168px;height:38px;line-height:38px;border-radius:19px;text-align:center;
  font-size:13px;font-weight:500;text-decoration:none}
.sample-primary{background:var(--white);color:var(--ink)}
.sample-legacy{background:var(--accent);color:var(--white)}

.signup{position:absolute;left:0;top:632px;width:1200px;height:182px;
  background:linear-gradient(180deg,var(--navy) 0%,var(--navy) 70%,var(--navy-low) 100%)}
.balloon{position:absolute;top:24px;width:72px;height:92px;border-radius:50% 50% 45% 45%;
  background:radial-gradient(circle at 40% 35%,#4a4f86,#262b58)}
.balloon-left{left:139px}.balloon-right{left:991px}
.signup h2{position:absolute;left:0;top:32px;width:1200px;text-align:center;color:var(--white);font-size:21px;font-weight:500}
.signup-form{position:absolute;left:292px;top:74px;width:616px;height:51px;display:flex;border-radius:26px;overflow:hidden}
.signup-form .email{flex:0 0 450px;border:0;background:var(--white);padding-left:21px;font:13px 'Roboto',sans-serif;color:#888}
.signup-form .subscribe{flex:1;border:0;background:var(--accent);color:var(--white);font:500 16px 'Roboto',sans-serif}
.signin{position:absolute;left:0;top:145px;width:1200px;text-align:center;color:#d8dbe6;font-size:12.5px}
.signin a{color:var(--white);font-size:16px;margin-left:8px}

.features{position:absolute;left:0;top:814px;width:1200px;height:218px;display:flex}
.feature{position:relative;width:240px;height:218px;display:flex;align-items:center;justify-content:center;text-align:center}
.feature:nth-child(1),.feature:nth-child(5){background:var(--tile-a)}
.feature:nth-child(2),.feature:nth-child(4){background:var(--tile-b)}
.feature:nth-child(3){background:var(--tile-c)}
.feature-mark{position:absolute;left:50%;top:50%;width:150px;height:150px;margin:-75px 0 0 -75px;border-radius:50%;
  background:rgba(255,255,255,.07)}
.feature p{position:relative;color:var(--white);font-size:19px;font-weight:300;line-height:23px;padding:0 10px}
.feature strong{font-weight:500}

.footer{position:absolute;left:0;top:1032px;width:1200px;height:54px;background:var(--footer);
  color:var(--white);font-size:12.5px;text-align:center;line-height:54px}
</style>
</head>
<body>
<header class="hero">
  <div class="hero-art" role="img" aria-label="Faint illustration of a leafy family tree spreading across the background"></div>
  <nav class="nav-links"><a href="#">Blog</a><a href="#">Podcast</a></nav>
  <nav class="account-links"><a href="#">Sign up</a><a href="#">Log in</a></nav>
  <div class="ring ring-outer"></div>
  <div class="ring ring-mid"></div>
  <div class="ring disc"></div>
  <div class="intro">
    <span class="brand-name">Quorvel</span>
    <p><em>Build</em> multiple Quorvel pages through one account for yourself, your family and to keep loved one's legacies alive.</p>
  </div>
  <div class="samples"><a class="sample-primary" href="#">Sample Quorvel Profile</a><a class="sample-legacy" href="#">Sample Legacy Profile</a></div>
</header>

<section class="signup">
  <div class="balloon balloon-left" role="img" aria-label="Hot air balloon illustration"></div>
  <div class="balloon balloon-right" role="img" aria-label="Hot air balloon illustration"></div>
  <h2>Become an Early User</h2>
  <form class="signup-form"><input class="email" type="text" placeholder="Type Your Email Adress"><button class="subscribe" type="button">Subscribe</button></form>
  <div class="signin">Already Have an Account? <a href="#">Sign in</a></div>
</section>

<section class="features">
  <div class="feature"><div class="feature-mark" role="img" aria-label="Faint pencil icon"></div><p><strong>Create</strong> Timelines, Maps,<br>Family Trees</p></div>
  <div class="feature"><div class="feature-mark" role="img" aria-label="Faint heart icon"></div><p><strong>Memorialize</strong> Loved<br>Ones</p></div>
  <div class="feature"><div class="feature-mark" role="img" aria-label="Faint share icon"></div><p><strong>Share</strong> Family Stories,<br>History and more Maps,</p></div>
  <div class="feature"><div class="feature-mark" role="img" aria-label="Faint eye icon"></div><p><strong>Control</strong> Your<br>Privacy</p></div>
  <div class="feature"><div class="feature-mark" role="img" aria-label="Faint crossed-out megaphone icon"></div><p><strong>No</strong> Ads, No Like Buttons<br><strong>No</strong> News Feeds</p></div>
</section>

<footer class="footer">Copyright © 2017 Quorvel All Rights Reserved.</footer>
</body>
</html>
```